Larkfield milling Business Card Design

Rice milling

Industry/Entity Type

Business

Contact Information for Business Card

DALE VOSKO
Construction Manager
LARKFIELD MILLING CO., LLC
3870 WILBUR HASTINGS DRIVE
MAPLE BEND, AR 72999
CELL: 501-555-0142
dalevosko@larkfieldmills.example

```html
<!DOCTYPE html>
<html lang="en">
<head>
<meta charset="utf-8">
<title>Larkfield Milling – Business Card</title>
<link href="https://fonts.googleapis.com/css2?family=Open+Sans:wght@400;600;700&family=Fira+Sans+Condensed:wght@400;500&display=swap" rel="stylesheet">
<style>
  :root {
    --teal: #0f9488;
    --teal-deep: #0b7368;
    --teal-dark: #085d55;
    --ink: #3a3a3a;
    --rule: #4a4a4a;
    --paper: #ffffff;
    --stage: #ecebe7;
  }
  * { box-sizing: border-box; margin: 0; padding: 0; }
  html, body {
    width: 1200px; height: 1024px; overflow: hidden;
    background: var(--stage);
    font-family: "Open Sans", Arial, sans-serif;
  }
  .sheet {
    position: relative; width: 1200px; height: 1024px;
    display: flex; flex-direction: column; align-items: center; justify-content: center;
    gap: 40px;
  }
  .card {
    position: relative; width: 760px; height: 434px;
    border-radius: 4px; overflow: hidden;
    box-shadow: 0 6px 18px rgba(0,0,0,.12);
  }

  /* Front */
  .card-front { background: var(--paper); }
  .brand-name {
    font-family: "Open Sans", Arial, sans-serif; font-weight: 600;
    color: var(--teal); letter-spacing: 1px; white-space: nowrap; line-height: 1;
  }
  .card-front .brand-name {
    position: absolute; left: 58px; top: 104px; font-size: 30px;
  }
  .person { position: absolute; right: 50px; top: 82px; }
  .person-name {
    font-family: "Fira Sans Condensed", Arial, sans-serif; font-weight: 500;
    color: var(--teal); font-size: 34px; line-height: 1;
  }
  .person-title {
    font-family: "Fira Sans Condensed", Arial, sans-serif;
    color: var(--ink); font-size: 15px; margin-top: 6px;
  }
  .rule-top {
    position: absolute; left: 410px; width: 128px; top: 118px;
    height: 1px; background: var(--rule);
  }
  .rule-mid {
    position: absolute; left: 58px; right: 50px; top: 206px;
    height: 1px; background: var(--rule);
  }
  .contacts {
    position: absolute; left: 60px; top: 232px; list-style: none;
    font-size: 16px; color: var(--ink);
  }
  .contacts li { display: flex; align-items: flex-start; gap: 14px; margin-bottom: 11px; line-height: 1.35; }
  .contacts svg { flex: none; width: 20px; height: 20px; margin-top: 1px; }

  /* Back */
  .card-back {
    background: radial-gradient(ellipse at 40% 35%, #14a394 0%, var(--teal) 45%, var(--teal-deep) 100%);
  }
  .card-back .brand-name {
    position: absolute; left: 0; right: 0; top: 190px; text-align: center;
    color: var(--paper); font-size: 46px;
  }
  .web {
    position: absolute; left: 0; right: 0; bottom: 46px; text-align: center;
    color: var(--paper); font-size: 15px; letter-spacing: 7px;
  }
  .tab { position: absolute; width: 140px; height: 22px; background: var(--teal-dark); }
  .tab-left { left: 0; top: 36px; }
  .tab-right { right: 0; bottom: 36px; }
</style>
</head>
<body>
<main class="sheet">

  <section class="card card-front" aria-label="Business card front">
    <div class="brand-name">LARKFIELD MILLING</div>
    <div class="rule-top"></div>
    <div class="person">
      <div class="person-name">Dale Vosko</div>
      <div class="person-title">Construction Manager</div>
    </div>
    <div class="rule-mid"></div>
    <ul class="contacts">
      <li>
        <svg viewBox="0 0 20 20"><rect x="5" y="1" width="10" height="18" rx="2" fill="var(--teal)"/><rect x="7" y="4" width="6" height="10" fill="#fff"/></svg>
        501-555-0142
      </li>
      <li>
        <svg viewBox="0 0 20 20"><rect x="1" y="4" width="18" height="12" rx="2" fill="var(--teal)"/><path d="M2 5l8 6 8-6" stroke="#fff" stroke-width="1.5" fill="none"/></svg>
        dalevosko@larkfieldmills.example
      </li>
      <li>
        <svg viewBox="0 0 20 20"><circle cx="10" cy="10" r="9" fill="var(--teal)"/><path d="M1 10h18M10 1c-4 4-4 14 0 18M10 1c4 4 4 14 0 18" stroke="#fff" stroke-width="1.2" fill="none"/></svg>
        www.larkfieldmills.example
      </li>
      <li>
        <svg viewBox="0 0 20 20"><path d="M10 1a6 6 0 0 0-6 6c0 5 6 12 6 12s6-7 6-12a6 6 0 0 0-6-6z" fill="var(--teal)"/><circle cx="10" cy="7" r="2.2" fill="#fff"/></svg>
        3870 WILBUR HASTINGS DRIVE MAPLE BEND,<br>AR 72999
      </li>
    </ul>
  </section>

  <section class="card card-back" aria-label="Business card back">
    <div class="tab tab-left"></div>
    <div class="brand-name">LARKFIELD MILLING</div>
    <div class="web">www.larkfieldmills.example</div>
    <div class="tab tab-right"></div>
  </section>

</main>
</body>
</html>
```